Terravane Business Card Design

We need a modern, clean, business card design for our hardscape solution company. I have outlined our specialist areas in the card information section. We meet and greet and wish to build relationships with large-scale builders and project managers of large-scale building companies. Hence the reason for the business card.We want them to understand we are their 'solution' and we will make their working life easier and less stressful. We also are the highest quality construction with an exceptional eye for detail taking a lot of pressure off the project managers. I have done a few mock-ups myself but would like to see what else can be created. We are open to black or white (or grey) background.

Industry/Entity Type

Construction

Contact Information for Business Card

Mark Quinlow - Director
0417 583 902
mark@terravanegroup.com

www.terravanegroup.com.au

"Hardscape Construction Solutions for Large-Scale Builders" (front)

Logo already designed and to be added.

REAR:

Your One-Stop Hardscape Solution For:

Retirement Village & Community Development Construction

- Synthetic Sports Fields - Bowling Greens
- Tennis Courts - Concreting
- Paving - Landscape

www.terravanegroup.com

```html
<!DOCTYPE html>
<html lang="en">
<head>
<meta charset="utf-8">
<title>Terravane Business Card</title>
<link rel="stylesheet" href="https://fonts.googleapis.com/css2?family=Source+Sans+3:wght@400;600;700&display=swap">
<style>
  :root {
    --stage: #1d1d1f;
    --card-white: #f3f3f5;
    --silver-dark: #a9aaad;
    --silver-light: #ececec;
    --ink: #111111;
    --ink-soft: #4a4a4a;
    --grey-text: #6f6f72;
    --brand-blue: #1a9ad6;
    --icon-blue: #1f86c9;
  }
  * { box-sizing: border-box; margin: 0; padding: 0; }
  html, body {
    width: 1200px; height: 1200px; overflow: hidden;
    background: var(--stage);
    font-family: "Source Sans 3", "Myriad Pro", sans-serif;
  }
  .canvas { position: relative; width: 1200px; height: 1200px; }

  .card { position: absolute; left: 216px; width: 766px; height: 462px; overflow: hidden; }

  /* Front */
  .card-front {
    top: 122px;
    border-radius: 0 36px 0 36px;
    background: linear-gradient(90deg, #c9c9cc 0, #ececee 5%, var(--card-white) 14%, var(--card-white) 100%);
  }
  .holder { position: absolute; left: 90px; top: 70px; }
  .holder-name { font-size: 25px; font-weight: 700; color: var(--ink); line-height: 1; }
  .holder-role { font-size: 19px; color: var(--ink-soft); margin-top: 5px; }
  .front-brand {
    position: absolute; right: 44px; top: 44px;
    font-size: 52px; font-weight: 600; color: var(--brand-blue); line-height: 1;
  }
  .contact-list { position: absolute; right: 28px; top: 248px; list-style: none; }
  .contact-item {
    display: flex; align-items: center; justify-content: flex-end; gap: 8px;
    font-size: 18px; color: var(--ink); height: 25px;
  }
  .contact-icon { width: 19px; height: 19px; }
  .tagline {
    position: absolute; left: 0; right: 0; top: 422px; text-align: center;
    font-size: 18px; color: var(--grey-text); padding-left: 36px;
  }

  /* Back */
  .card-back {
    top: 594px;
    border-radius: 36px 0 36px 0;
    background: radial-gradient(ellipse 60% 55% at 50% 45%, var(--silver-light) 0, #cfd0d2 60%, var(--silver-dark) 100%);
  }
  .logo-band {
    position: absolute; left: 40px; right: 40px; top: 42px; height: 192px;
    background: radial-gradient(ellipse 55% 70% at 50% 55%, #f6f6f6 0, #dcdcde 70%, rgba(210,210,212,0.6) 100%);
  }
  .back-brand {
    position: absolute; left: 0; right: 0; top: 86px; text-align: center;
    font-size: 104px; font-weight: 600; color: var(--brand-blue); line-height: 1;
  }
  .services-intro { position: absolute; left: 91px; top: 288px; font-size: 18px; color: var(--ink); }
  .services-lead { position: absolute; left: 124px; top: 326px; font-size: 18px; color: var(--ink); }
  .services-grid {
    position: absolute; left: 102px; top: 356px; list-style: none;
    display: grid; grid-template-columns: 232px 170px 170px; row-gap: 9px;
  }
  .service { display: flex; align-items: center; gap: 5px; font-size: 18px; color: var(--ink); }
  .service-bullet { width: 18px; height: 18px; flex: none; }
  .back-web {
    position: absolute; left: 0; right: 0; top: 424px; text-align: center;
    font-size: 17px; color: #ffffff;
  }
</style>
</head>
<body>
<main class="canvas">

  <section class="card card-front" aria-label="Business card front">
    <div class="holder">
      <p class="holder-name">Mark Quinlow</p>
      <p class="holder-role">Director</p>
    </div>
    <p class="front-brand">Terravane</p>

    <ul class="contact-list">
      <li class="contact-item">0417 583 902
        <svg class="contact-icon" viewBox="0 0 20 20" aria-hidden="true"><circle cx="10" cy="10" r="10" fill="var(--icon-blue)"/><path d="M6 6.5c0 4 3.5 7.5 7.5 7.5l1-2-2-1-1 1c-1.3-.6-2.4-1.7-3-3l1-1-1-2z" fill="#fff"/></svg>
      </li>
      <li class="contact-item">mark@terravanegroup.com
        <svg class="contact-icon" viewBox="0 0 20 20" aria-hidden="true"><circle cx="10" cy="10" r="10" fill="var(--icon-blue)"/><rect x="5" y="6.5" width="10" height="7" fill="none" stroke="#fff" stroke-width="1.3"/><path d="M5 6.5l5 4 5-4" fill="none" stroke="#fff" stroke-width="1.3"/></svg>
      </li>
      <li class="contact-item">www.terravanegroup.com.au
        <svg class="contact-icon" viewBox="0 0 20 20" aria-hidden="true"><circle cx="10" cy="10" r="10" fill="var(--icon-blue)"/><circle cx="10" cy="10" r="5.5" fill="none" stroke="#fff" stroke-width="1.2"/><ellipse cx="10" cy="10" rx="2.3" ry="5.5" fill="none" stroke="#fff" stroke-width="1.1"/><path d="M4.5 10h11" stroke="#fff" stroke-width="1.1"/></svg>
      </li>
    </ul>

    <p class="tagline">Hardscape Construction Solutions for Large-Scale Builders</p>
  </section>

  <section class="card card-back" aria-label="Business card back">
    <div class="logo-band"></div>
    <p class="back-brand">Terravane</p>

    <p class="services-intro">Your One-Stop Hardscape Solution For:</p>
    <p class="services-lead">Retirement Village &amp; Community Development Construction</p>

    <ul class="services-grid">
      <li class="service"><svg class="service-bullet" viewBox="0 0 20 20" aria-hidden="true"><circle cx="10" cy="10" r="10" fill="var(--icon-blue)"/><path d="M6 10h7M10 6.5l3.5 3.5-3.5 3.5" fill="none" stroke="#fff" stroke-width="1.8"/></svg>Synthetic Sports Fields</li>
      <li class="service"><svg class="service-bullet" viewBox="0 0 20 20" aria-hidden="true"><circle cx="10" cy="10" r="10" fill="var(--icon-blue)"/><path d="M6 10h7M10 6.5l3.5 3.5-3.5 3.5" fill="none" stroke="#fff" stroke-width="1.8"/></svg>Bowling Greens</li>
      <li class="service"><svg class="service-bullet" viewBox="0 0 20 20" aria-hidden="true"><circle cx="10" cy="10" r="10" fill="var(--icon-blue)"/><path d="M6 10h7M10 6.5l3.5 3.5-3.5 3.5" fill="none" stroke="#fff" stroke-width="1.8"/></svg>Tennis Courts</li>
      <li class="service"><svg class="service-bullet" viewBox="0 0 20 20" aria-hidden="true"><circle cx="10" cy="10" r="10" fill="var(--icon-blue)"/><path d="M6 10h7M10 6.5l3.5 3.5-3.5 3.5" fill="none" stroke="#fff" stroke-width="1.8"/></svg>Concreting</li>
      <li class="service"><svg class="service-bullet" viewBox="0 0 20 20" aria-hidden="true"><circle cx="10" cy="10" r="10" fill="var(--icon-blue)"/><path d="M6 10h7M10 6.5l3.5 3.5-3.5 3.5" fill="none" stroke="#fff" stroke-width="1.8"/></svg>Paving</li>
      <li class="service"><svg class="service-bullet" viewBox="0 0 20 20" aria-hidden="true"><circle cx="10" cy="10" r="10" fill="var(--icon-blue)"/><path d="M6 10h7M10 6.5l3.5 3.5-3.5 3.5" fill="none" stroke="#fff" stroke-width="1.8"/></svg>Landscape</li>
    </ul>

    <p class="back-web">www.terravanegroup.com</p>
  </section>

</main>
</body>
</html>
```